R J Penn Accounting & SMSF Auditing needs a Web Site Design

I need some examples of what a web design can look like for my business.
The business name is above and I have already registered a domain name of www.penn-smsf.com.au
I have attached my current letterhead and business cards and would like to maintain these colours basically Red on White with some black

```html
<!DOCTYPE html>
<html lang="en">
<head>
<meta charset="utf-8">
<title>Accounting &amp; Fund Auditing – Home</title>
<link rel="stylesheet" href="https://fonts.googleapis.com/css2?family=Roboto+Condensed:wght@400;700&family=Roboto:wght@400;700&family=Libre+Baskerville&display=swap">
<style>
:root{
  --red:#c8102e;
  --ink:#1d1d1d;
  --text:#444;
  --muted:#888;
  --white:#fff;
  --teal:#2f3e3f;
  --footer:#1c1c1c;
  --line:#ddd;
}
*{margin:0;padding:0;box-sizing:border-box}
html,body{width:1200px;height:2471px;overflow:hidden}
body{position:relative;background:var(--white);font-family:"Roboto",Arial,sans-serif;color:var(--text)}
.abs{position:absolute}
.cond{font-family:"Roboto Condensed","Arial Narrow",sans-serif}

/* hero */
.hero{left:0;top:0;width:1200px;height:673px;background:linear-gradient(100deg,#5a2e1c 0%,#8a5a3c 35%,#c9a27a 60%,#7a4a30 85%,#3e2215 100%)}
.topbar{left:0;top:0;width:1200px;height:11px;background:var(--ink)}
.header{left:0;top:11px;width:1200px;height:96px;background:rgba(255,255,255,.86)}
.brand{left:150px;top:30px;font-size:34px;font-weight:400;color:var(--ink);letter-spacing:2px}
.nav{right:160px;top:50px;display:flex;gap:38px;font-size:15px;color:#333;text-transform:uppercase}
.hero-title{left:192px;top:296px;font-size:50px;font-weight:700;color:var(--white)}
.hero-sub{left:192px;top:360px;font-size:37px;line-height:54px;color:var(--white);text-transform:uppercase}
.btn{top:502px;height:52px;display:flex;align-items:center;justify-content:center;font-size:27px;color:var(--white);text-transform:uppercase;border:2px solid var(--white)}
.btn-red{left:192px;width:226px;background:var(--red)}
.btn-dark{left:434px;width:228px;background:#111}

/* welcome */
.welcome{left:0;top:673px;width:1200px;height:294px;background:var(--red);color:var(--white)}
.welcome h2{position:absolute;left:184px;top:34px;font-size:44px;font-weight:400}
.welcome p{position:absolute;left:184px;top:112px;width:834px;font-size:14.5px;line-height:22px}

/* services */
.tile{top:1010px;width:261px;height:152px}
.tile-label{position:absolute;left:0;bottom:10px;padding:6px 14px;background:var(--red);color:var(--white);font-size:20px;text-transform:uppercase}
.box{top:1200px;height:343px;border:1px solid var(--line);background:var(--white);overflow:hidden}
.box-head{height:60px;background:var(--red);color:var(--white);display:flex;align-items:center;padding-left:22px;font-size:27px;text-transform:uppercase}
.box p{font-size:12.5px;line-height:19px;color:var(--text)}
.portrait{position:absolute;left:60px;top:80px;width:175px;height:240px;background:linear-gradient(#e4e4e4,#3a3a3a)}
.feature{position:absolute;left:256px;top:82px;width:290px}
.feature h3{font-size:20px;color:var(--ink);margin-bottom:10px;display:flex;align-items:center;gap:12px}
.feature h3::before{content:"";width:9px;height:9px;background:var(--red)}
.pager{position:absolute;right:12px;bottom:12px;display:flex;gap:4px}
.pager span{width:24px;height:24px;border:1px solid var(--line);display:flex;align-items:center;justify-content:center;font-size:14px;color:var(--muted)}
.list{padding:16px 16px 0 18px}
.list li{list-style:none;position:relative;padding-left:18px;margin-bottom:14px;font-size:12px;line-height:18px}
.list li::before{content:"";position:absolute;left:0;top:6px;width:7px;height:7px;background:var(--red)}

/* team */
.team{left:0;top:1587px;width:1200px;height:459px;background:var(--teal)}
.team h2{position:absolute;left:0;top:38px;width:1200px;text-align:center;font-size:40px;font-weight:400;color:var(--white)}
.card{top:1722px;width:187px;height:272px;background:var(--white);text-align:center}
.card .photo{width:118px;height:118px;border-radius:50%;margin:20px auto 0;background:linear-gradient(#d9d2c8,#7d6f64)}
.card h4{margin-top:22px;font-size:13px;letter-spacing:1px;color:var(--ink)}
.card .role{font-size:10px;color:var(--muted);margin-top:4px}
.card p{font-size:11px;line-height:15px;color:var(--muted);padding:14px 16px 0}

/* testimonials */
.testi-title{left:0;top:2080px;width:1200px;text-align:center;font-size:40px;color:var(--ink);font-weight:400}
.testi-photo{top:2190px;width:118px;height:163px;background:linear-gradient(#cfcfcf,#222)}
.testi h3{font-family:"Libre Baskerville",Georgia,serif;font-size:25px;font-weight:400;color:var(--ink)}
.testi p{font-family:"Libre Baskerville",Georgia,serif;font-size:15px;line-height:21px;color:var(--text);margin-top:10px;width:250px}
.divider{left:599px;top:2160px;width:1px;height:190px;background:var(--line)}

/* footer */
.footer{left:0;top:2353px;width:1200px;height:118px;background:var(--footer)}
.fnav{left:266px;top:2353px;height:62px;display:flex;font-size:13px;color:#ccc;text-transform:uppercase}
.fnav span{display:flex;align-items:center;padding:0 17px}
.fnav .active{background:var(--red);color:var(--white)}
.social{left:904px;top:2372px;display:flex;gap:8px}
.social span{width:28px;height:28px;background:#5d6f86}
.legal{left:0;top:2434px;width:1200px;text-align:center;font-size:12px;color:#999}
</style>
</head>
<body>

<div class="abs hero" role="img" aria-label="Courtroom backdrop with brass scales of justice"></div>
<div class="abs topbar"></div>
<header class="abs header">
  <div class="abs brand cond">PENN AUDIT</div>
  <nav class="abs nav cond"><span>Home</span><span>Our Firm</span><span>Attoneys</span><span>Deals &amp; Cases</span><span>Case Result</span><span>Contact Us</span></nav>
</header>
<h1 class="abs hero-title cond">LOREM IPSUM DOLOR</h1>
<div class="abs hero-sub cond">Lorem ipsum dolor sit amet,<br>consectetur adipiscing eli</div>
<div class="abs btn btn-red cond">Lorem ipsum</div>
<div class="abs btn btn-dark cond">Lorem ipsum</div>

<section class="abs welcome">
  <h2 class="cond">WELCOME</h2>
  <p>Sed ut perspiciatis unde omnis iste natus error sit voluptatem accusantium doloremque laudantium, totam rem aperiam, eaque ipsa quae ab illo inventore veritatis et quasi architecto beatae vitae dicta sunt explicabo. Nemo enim ipsam voluptatem quia voluptas sit aspernatur aut odit aut fugit, sed quia consequuntur magni dolores eos qui ratione voluptatem sequi nesciunt. Neque porro quisquam est, qui dolorem ipsum quia dolor sit amet, consectetur, adipisci velit, sed quia non numquam eius modi tempora incidunt ut labore et dolore magnam aliquam quaerat voluptatem. Ut enim ad minima veniam, quis nostrum exercitationem ullam corporis suscipit laboriosam, nisi ut aliquid ex ea commodi consequatur? Nemo enim ipsam voluptatem quia voluptas.</p>
</section>

<div class="abs tile" style="left:178px;background:linear-gradient(#6b4a3a,#3b2418)" role="img" aria-label="Law book and gavel"><span class="tile-label cond">Lorem ipsum</span></div>
<div class="abs tile" style="left:467px;background:linear-gradient(#d8b36a,#6a4a22)" role="img" aria-label="Gavel resting on a legal document"><span class="tile-label cond">Lorem ipsum</span></div>
<div class="abs tile" style="left:758px;background:linear-gradient(#f1f1f1,#9aa0a8)" role="img" aria-label="Business team at the office"><span class="tile-label cond">Lorem ipsum</span></div>

<div class="abs box" style="left:168px;width:562px">
  <div class="box-head cond">Lorem ipsum dolor sit amet</div>
  <div class="portrait" role="img" aria-label="Senior lawyer holding a book"></div>
  <div class="feature">
    <h3 class="cond">Lorem ipsum dolor</h3>
    <p>Lorem ipsum dolor sit amet, consectetur adipiscing elit, sed do eiusmod tempor incididunt ut labore et dolore magna aliqua. Ut enim ad minim veniam, quis nostrud exercitation ullamco laboris nisi ut aliquip ex ea commodo consequat. Duis aute irure dolor in reprehenderit.</p>
    <p style="margin-top:4px">Lorem ipsum dolor sit amet, consectetur adipiscing elit, sed do eiusmod tempor incididunt ut labore et dolore magna aliqua.</p>
  </div>
  <div class="pager"><span>&#8249;</span><span>&#8250;</span></div>
</div>

<div class="abs box" style="left:758px;width:264px">
  <div class="box-head cond" style="font-size:23px">Lorem ipsum dolor</div>
  <ul class="list">
    <li>Lorem ipsum dolor sit amet, consectetur adipiscing elit, sed do eiusmod tempor incididunt ut labore et dolore magna aliqua.</li>
    <li>Lorem ipsum dolor sit amet, consectetur adipiscing elit, sed do eiusmod tempor incididunt ut labore et dolore.</li>
    <li>Lorem ipsum dolor sit amet, consectetur adipiscing elit, sed do eiusmod tempor.</li>
  </ul>
</div>

<section class="abs team"><h2 class="cond">LOREM IPSUM DOLOR</h2></section>
<div class="abs card" style="left:170px"><div class="photo" role="img" aria-label="Portrait of Oliver Hartley"></div><h4 class="cond">OLIVER HARTLEY</h4><div class="role">Senior Lawyer</div><p>A team member with years of practice in trust law and fund audits, known for clear advice.</p></div>
<div class="abs card" style="left:395px"><div class="photo" role="img" aria-label="Portrait of Claire Morton"></div><h4 class="cond">CLAIRE MORTON</h4><div class="role">Senior Lawyer</div><p>A team member with years of practice in trust law and fund audits, known for clear advice.</p></div>
<div class="abs card" style="left:620px"><div class="photo" role="img" aria-label="Portrait of Sophie Whitlam"></div><h4 class="cond">SOPHIE WHITLAM</h4><div class="role">Senior Lawyer</div><p>A team member with years of practice in trust law and fund audits, known for clear advice.</p></div>
<div class="abs card" style="left:846px"><div class="photo" role="img" aria-label="Portrait of Graham Fenwick"></div><h4 class="cond">GRAHAM FENWICK</h4><div class="role">Senior Lawyer</div><p>A team member with years of practice in trust law and fund audits, known for clear advice.</p></div>

<h2 class="abs testi-title cond">TESTIMONIAL</h2>
<div class="abs testi-photo" style="left:196px" role="img" aria-label="Smiling businesswoman"></div>
<div class="abs testi" style="left:322px;top:2200px"><h3>Sed Ut Perspiciatis</h3><p>&ldquo;Sed ut perspiciatis unde omnis iste error sit voluptatem accusantium.&rdquo;</p></div>
<div class="abs divider"></div>
<div class="abs testi-photo" style="left:660px" role="img" aria-label="Smiling businessman"></div>
<div class="abs testi" style="left:786px;top:2200px"><h3>Sed Ut Perspiciatis</h3><p>&ldquo;Sed ut perspiciatis unde omnis iste error sit voluptatem accusantium.&rdquo;</p></div>

<footer class="abs footer"></footer>
<nav class="abs fnav cond"><span class="active">Home</span><span>Our Firm</span><span>Attoneys</span><span>Deals &amp; Cases</span><span>Case Result</span><span>Contact Us</span></nav>
<div class="abs social" aria-label="Social links"><span></span><span></span><span></span><span></span></div>
<div class="abs legal">Privacy | Copyright</div>

</body>
</html>
```